New vaporizer packaging (box) requirements

We need both the top and bottom of a box created. We have mock ups of the die lines,the photograph we want used on the top of the box, the product details needed for the bottom of the box. Lots more detail listed on each attached file. We need YOU to help us put our ideas together!

```html
<!DOCTYPE html>
<html lang="en">
<head>
<meta charset="utf-8">
<title>Nimbra Tempest – Box Dieline</title>
<link rel="stylesheet" href="https://fonts.googleapis.com/css2?family=Cinzel:wght@600&family=Russo+One&family=Montserrat:wght@500&display=swap">
<style>
  :root {
    --backdrop: #e2e3e4;
    --panel-black: #050505;
    --leaf-deep: #0b1a0a;
    --leaf-mid: #1f3d17;
    --band-orange: #f39a1e;
    --brand-white: #f4f4f4;
    --product-red: #d9261c;
    --window-fill: #020202;
    --window-line: #c4161c;
    --window-label: #4a4a4a;
    --guide-line: #7d9a2a;
    --glow: #ff8a1a;
  }
  html, body {
    margin: 0;
    padding: 0;
    width: 1003px;
    height: 1200px;
    overflow: hidden;
    background: var(--backdrop);
  }
  .dieline {
    display: block;
    width: 1003px;
    height: 1200px;
  }
  .brand-name {
    font-family: "Cinzel", serif;
    font-weight: 600;
    fill: var(--brand-white);
    letter-spacing: 2px;
  }
  .product-name {
    font-family: "Russo One", sans-serif;
    fill: var(--product-red);
    letter-spacing: 1px;
  }
  .window-label {
    font-family: "Montserrat", sans-serif;
    font-weight: 500;
    fill: var(--window-label);
  }
</style>
</head>
<body>
<svg class="dieline" viewBox="0 0 1003 1200" xmlns="http://www.w3.org/2000/svg">
  <defs>
    <linearGradient id="leafPhoto" x1="0" y1="0" x2="1" y2="1">
      <stop offset="0" stop-color="var(--leaf-mid)"/>
      <stop offset="0.35" stop-color="var(--leaf-deep)"/>
      <stop offset="0.65" stop-color="var(--leaf-mid)"/>
      <stop offset="1" stop-color="var(--leaf-deep)"/>
    </linearGradient>
    <radialGradient id="sideGlow" cx="0.5" cy="0.5" r="0.5">
      <stop offset="0" stop-color="var(--glow)" stop-opacity="0.55"/>
      <stop offset="1" stop-color="var(--glow)" stop-opacity="0"/>
    </radialGradient>
  </defs>

  <g class="box-flat" transform="translate(0 270)">
    <!-- Centre column: top flap, front face, bottom flap share one photo area -->
    <path class="leaf-photo" role="img" aria-label="Dark photograph of green cannabis leaves filling the box lid"
          d="M204 12 L500 36 L802 12 L802 630 L802 648 L500 622 L204 648 Z"
          fill="url(#leafPhoto)"/>

    <!-- Orange border bands -->
    <path class="edge-band edge-band--top" role="img" aria-label="Orange border band with key pattern"
          d="M204 12 L500 36 L802 12 L802 30 L500 54 L204 30 Z" fill="var(--band-orange)"/>
    <path class="edge-band edge-band--bottom" role="img" aria-label="Orange border band with key pattern"
          d="M204 630 L500 604 L802 630 L802 648 L500 622 L204 648 Z" fill="var(--band-orange)"/>

    <!-- Side panels -->
    <rect class="side-panel side-panel--left" x="10" y="206" width="194" height="248" fill="var(--panel-black)"/>
    <rect class="side-panel side-panel--right" x="802" y="206" width="192" height="248" fill="var(--panel-black)"/>
    <ellipse cx="80" cy="330" rx="40" ry="90" fill="url(#sideGlow)"/>
    <ellipse cx="924" cy="330" rx="40" ry="90" fill="url(#sideGlow)"/>

    <!-- Front face guide -->
    <rect class="front-guide" x="210" y="212" width="584" height="234" fill="none" stroke="var(--guide-line)" stroke-width="0.8"/>

    <!-- Clear window -->
    <path class="clear-window"
          d="M256 284 H724 V298 L732 304 H752 Q756 304 756 308 V348 Q756 352 752 352 H732 L724 358 V374 H256 Q248 374 248 366 V292 Q248 284 256 284 Z"
          fill="var(--window-fill)" stroke="var(--window-line)" stroke-width="1"/>
    <text class="window-label" x="498" y="337" font-size="20" text-anchor="middle">Clear Window</text>

    <!-- Front face branding -->
    <text class="brand-name" x="258" y="266" font-size="38">Nimbra</text>
    <text class="product-name" x="500" y="432" font-size="52" text-anchor="middle">TEMPEST</text>

    <!-- Top flap (reads upside down) -->
    <text class="brand-name" x="0" y="0" font-size="44" text-anchor="middle"
          transform="translate(492 108) rotate(180)">Nimbra</text>

    <!-- Bottom flap -->
    <text class="brand-name" x="496" y="558" font-size="50" text-anchor="middle">Nimbra</text>

    <!-- Left side panel -->
    <text class="product-name" x="0" y="0" font-size="38" text-anchor="middle"
          transform="translate(66 330) rotate(90)">TEMPEST</text>
    <text class="brand-name" x="0" y="0" font-size="30" text-anchor="middle"
          transform="translate(116 330) rotate(90)">Nimbra</text>

    <!-- Right side panel -->
    <text class="product-name" x="0" y="0" font-size="38" text-anchor="middle"
          transform="translate(938 330) rotate(-90)">TEMPEST</text>
    <text class="brand-name" x="0" y="0" font-size="30" text-anchor="middle"
          transform="translate(886 330) rotate(-90)">Nimbra</text>
  </g>
</svg>
</body>
</html>
```